Corvana Dental Development - Business Cards

We are a Dental Development and Management company. We are looking to develop a new business card design. We are business professional but modern. The logo that I have attached is the business colors. You can also check out our website for further detail. www.corvanadentalmanagement.example

Target Market(s)

Dental Professionals, Dentists and Office Staff, Marketing Professionals

Industry/Entity Type

Business

Requirements
Must have
• Name - Dominic R. Hartwell
Title - Marketing Director
Phone - 555-014-2273
Cell - 555-014-2273
Email - Dom.h@Corvanadentaldevelopment.example
Address - 2918 W Larkspur Rd, Mesa, AZ 85213
Web- www.corvanadentaldevelopment.example

Corvana Logo must go on the front. The other logos go on the back as affiliated businesses

Must be editable to enter specific Names, Positions, Phone numbers and email later on. Using Adobe CS5 currently.

```html
<!DOCTYPE html>
<html lang="en">
<head>
<meta charset="utf-8">
<title>Corvana Dental Development – Business Cards</title>
<link rel="stylesheet" href="https://fonts.googleapis.com/css2?family=Lato:wght@400;700;900&display=swap">
<style>
  :root {
    --navy: #232a6b;
    --gold: #e39b2f;
    --ink: #2a2a3a;
    --card: #ffffff;
    --card-fade: #f1f1f5;
    --stage: #e4e4e7;
    --affiliate-green: #3f7f3a;
    --affiliate-red: #c0342c;
    --affiliate-sky: #3aa7d9;
  }
  * { box-sizing: border-box; margin: 0; padding: 0; }
  html, body { width: 1200px; height: 900px; overflow: hidden; }
  body {
    background: var(--stage);
    font-family: "Lato", sans-serif;
    color: var(--ink);
    position: relative;
  }
  .card {
    position: absolute;
    top: 295px;
    width: 508px;
    height: 308px;
    background: linear-gradient(180deg, var(--card) 0%, var(--card-fade) 100%);
    box-shadow: 0 2px 6px rgba(0,0,0,0.25);
    overflow: hidden;
  }
  .card--front { left: 77px; }
  .card--back { left: 615px; }
  .card__band {
    position: absolute; left: 0; right: 0; bottom: 0; height: 11px;
  }
  .card--front .card__band { background: var(--navy); }
  .card--back .card__band { background: var(--gold); }

  .brand {
    font-weight: 900;
    color: var(--navy);
    text-transform: uppercase;
    line-height: 1;
  }
  .brand__name { display: block; letter-spacing: 1px; }
  .brand__line { display: block; letter-spacing: 3px; }

  .card--front .brand {
    position: absolute; left: 0; right: 0; top: 118px; text-align: center;
  }
  .card--front .brand__name { font-size: 56px; }
  .card--front .brand__line { font-size: 20px; margin-top: 8px; }
  .card--front .web {
    position: absolute; left: 0; right: 0; top: 274px;
    text-align: center; font-size: 12px; color: var(--navy);
  }

  .card--back .brand { position: absolute; left: 32px; top: 48px; }
  .card--back .brand__name { font-size: 34px; }
  .card--back .brand__line { font-size: 12.5px; margin-top: 6px; letter-spacing: 2.4px; }

  .person { position: absolute; left: 40px; top: 151px; }
  .person__name { font-size: 16px; font-weight: 700; color: var(--navy); }
  .person__title { font-size: 11.5px; margin-top: 6px; }

  .contact { position: absolute; left: 42px; list-style: none; font-size: 11.5px; }
  .contact li { display: flex; align-items: center; height: 15px; }
  .contact svg { width: 10px; height: 10px; margin-right: 7px; fill: var(--navy); flex: none; }
  .contact--phone { top: 203px; }
  .contact--online { top: 262px; }

  .divider {
    position: absolute; left: 361px; top: 60px; width: 1.5px; height: 232px;
    background: var(--gold);
  }
  .affiliates {
    position: absolute; left: 368px; width: 140px; top: 58px;
    list-style: none; text-align: center;
  }
  .affiliate { height: 78px; display: flex; flex-direction: column; justify-content: center; align-items: center; }
  .affiliate__name { font-size: 15px; font-weight: 700; line-height: 1.1; }
  .affiliate__name small { display: block; font-size: 8.5px; letter-spacing: 1px; text-transform: uppercase; }
  .affiliate--centers .affiliate__name { color: var(--navy); }
  .affiliate--plan .affiliate__name { color: var(--affiliate-red); }
  .affiliate--kids .affiliate__name { color: var(--affiliate-sky); font-size: 17px; }
</style>
</head>
<body>
  <section class="card card--front">
    <div class="brand">
      <span class="brand__name">Corvana</span>
      <span class="brand__line">Dental Management</span>
    </div>
    <p class="web">www.corvanadentaldevelopment.example</p>
    <div class="card__band"></div>
  </section>

  <section class="card card--back">
    <div class="brand">
      <span class="brand__name">Corvana</span>
      <span class="brand__line">Dental Management</span>
    </div>

    <div class="person">
      <p class="person__name">Dominic R. Hartwell</p>
      <p class="person__title">Marketing Director</p>
    </div>

    <ul class="contact contact--phone">
      <li><svg viewBox="0 0 10 10"><path d="M5 0a3.5 3.5 0 0 0-3.5 3.5C1.5 6 5 10 5 10s3.5-4 3.5-6.5A3.5 3.5 0 0 0 5 0zm0 5a1.4 1.4 0 1 1 0-2.8A1.4 1.4 0 0 1 5 5z"/></svg>2918 W Larkspur Rd, Mesa, AZ 85213</li>
      <li><svg viewBox="0 0 10 10"><circle cx="5" cy="5" r="5"/><path d="M3.2 2.4l1 1-.5.7c.4.8 1 1.4 1.8 1.8l.7-.5 1 1-.6.8C4.8 7.1 2.9 5.2 2.5 3z" fill="#fff"/></svg>555-014-2273</li>
      <li><svg viewBox="0 0 10 10"><path d="M2.5 0h5a.8.8 0 0 1 .8.8v8.4a.8.8 0 0 1-.8.8h-5a.8.8 0 0 1-.8-.8V.8A.8.8 0 0 1 2.5 0zm.4 1.2v6.6h4.2V1.2z"/></svg>555-014-2273</li>
    </ul>

    <ul class="contact contact--online">
      <li><svg viewBox="0 0 10 10"><path d="M0 2h10v6H0z"/><path d="M0 2l5 3.5L10 2" fill="none" stroke="#fff" stroke-width=".8"/></svg>Dom.h@Corvanadentaldevelopment.example</li>
      <li><svg viewBox="0 0 10 10"><circle cx="5" cy="5" r="4.5" fill="none" stroke="#232a6b" stroke-width="1"/><ellipse cx="5" cy="5" rx="2" ry="4.5" fill="none" stroke="#232a6b" stroke-width=".8"/><path d="M.5 5h9" stroke="#232a6b" stroke-width=".8"/></svg>www.corvanadentaldevelopment.example</li>
    </ul>

    <div class="divider"></div>

    <ul class="affiliates">
      <li class="affiliate affiliate--centers"><p class="affiliate__name">Brightway<small>Dental Centers</small></p></li>
      <li class="affiliate affiliate--plan"><p class="affiliate__name">Brightway<small>Dental Plan</small></p></li>
      <li class="affiliate affiliate--kids"><p class="affiliate__name">Smilewise</p></li>
    </ul>

    <div class="card__band"></div>
  </section>
</body>
</html>
```